Bathroom Renovation Business card design needed

Bathroom, Kitchen & Laundry Renovations
Mainly complete bathroom renovations

Target Market(s)

people wanting a total bathroom renovations and other trades people

Industry/Entity Type

Business

Contact Information for Business Card

Dalby Bathrooms
Tomas Dalby
Mobile: 0438 207615
Licence no: 764519K
Email: dalbybathrooms@mailnest.example

Logo styles of interest
Lettermark Logo
Requirements
Must have
• the business card should be predominantly blue
Nice to have
• the DB logo featured in the business card will be used on tshirts,tax invoices , letters etc so the DB will be the main feature, and preferably blue
Should not have
• We found the red DB logo through google images. We understand that it cannot be exactly the same but we like how the DB is linked. The example business card is something we designed but we prefer more blues. Maybe different shades of blue.

```html
<!DOCTYPE html>
<html lang="en">
<head>
<meta charset="utf-8">
<title>Dalby Bathrooms – Business Card</title>
<link rel="stylesheet" href="https://fonts.googleapis.com/css2?family=Roboto+Condensed:wght@400;500;700&display=swap">
<style>
  :root {
    --brand-teal: #1b7489;
    --frame-teal: #1f7a8c;
    --mark-mist: #dde9ef;
    --card-white: #ffffff;
  }
  html, body {
    margin: 0;
    padding: 0;
    width: 1200px;
    height: 695px;
    overflow: hidden;
    background: var(--card-white);
  }
  .business-card {
    position: relative;
    width: 1200px;
    height: 695px;
    box-sizing: border-box;
    border: 6px solid var(--frame-teal);
    background: var(--card-white);
    font-family: "Roboto Condensed", "Arial Narrow", sans-serif;
    color: var(--brand-teal);
    overflow: hidden;
  }
  .monogram-backdrop {
    position: absolute;
    left: 88px;
    top: 360px;
    margin: 0;
    font-size: 300px;
    font-weight: 700;
    line-height: 1;
    letter-spacing: -6px;
    color: var(--mark-mist);
    user-select: none;
  }
  .card-details {
    position: absolute;
    right: 124px;
    top: 118px;
    text-align: right;
  }
  .company-name {
    margin: 0;
    font-size: 57px;
    font-weight: 500;
    line-height: 1.1;
  }
  .owner-name {
    margin: 10px 0 0;
    font-size: 46px;
    font-weight: 400;
    line-height: 1.1;
  }
  .contact-list {
    list-style: none;
    margin: 42px 0 0;
    padding: 0;
    font-size: 40px;
    line-height: 63px;
  }
</style>
</head>
<body>
  <div class="business-card">
    <p class="monogram-backdrop" aria-hidden="true">DB</p>
    <div class="card-details">
      <h1 class="company-name">Dalby Bathrooms</h1>
      <p class="owner-name">Tomas Dalby</p>
      <ul class="contact-list">
        <li class="contact-phone">0438 207615</li>
        <li class="contact-email">dalbybathrooms@mailnest.example</li>
        <li class="contact-licence">Lic No: 764519K</li>
      </ul>
    </div>
  </div>
</body>
</html>
```